" Nós fazemos a administração geral dos condomínios. O que envolve solução de conflitos, contratação de serviços, orçamentos, administração financeira, reuniões de condôminos, relatórios gerenciais, orientações diversas ao síndico, conselheiros e condôminos. "

```html
<!DOCTYPE html>
<html lang="pt-BR">
<head>
<meta charset="utf-8">
<title>Vila Prumo – Envelope</title>
<link href="https://fonts.googleapis.com/css2?family=Montserrat:wght@400;600&display=swap" rel="stylesheet">
<style>
  :root {
    --stage: #e4e4e4;
    --envelope: #1d4f80;
    --envelope-faint: #245a8d;
    --accent: #2aa9e0;
    --text-soft: #8ec4e8;
  }
  html, body {
    margin: 0;
    width: 1200px;
    height: 1200px;
    overflow: hidden;
    background: var(--stage);
    font-family: "Montserrat", sans-serif;
  }
  .envelope {
    position: absolute;
    left: 50px;
    top: 210px;
    width: 1100px;
    height: 780px;
    background: var(--envelope);
    overflow: hidden;
  }
  .flap-mark {
    position: absolute;
    left: 0;
    right: 0;
    top: 250px;
    text-align: center;
    font-weight: 600;
    font-size: 110px;
    letter-spacing: 8px;
    color: var(--envelope-faint);
  }
  .brand {
    position: absolute;
    left: 40px;
    top: 628px;
    display: flex;
    align-items: center;
    gap: 10px;
    font-weight: 600;
    font-size: 24px;
    color: var(--accent);
  }
  .brand-dot {
    width: 14px;
    height: 14px;
    border-radius: 50%;
    background: var(--accent);
  }
  .contact {
    position: absolute;
    top: 616px;
    display: flex;
    gap: 12px;
    font-size: 15px;
    line-height: 1.5;
    color: var(--text-soft);
  }
  .contact svg { flex: none; margin-top: 3px; }
  .contact--address { left: 300px; }
  .contact--phone { left: 760px; }
  .rule {
    position: absolute;
    left: 40px;
    right: 0;
    top: 700px;
    height: 3px;
    background: var(--accent);
  }
  .email {
    position: absolute;
    left: 40px;
    top: 720px;
    font-size: 22px;
    letter-spacing: 6px;
    color: var(--text-soft);
  }
</style>
</head>
<body>
  <div class="envelope">
    <div class="flap-mark">VILA PRUMO</div>

    <div class="brand"><span class="brand-dot"></span>Vila Prumo</div>

    <div class="contact contact--address">
      <svg width="18" height="18" viewBox="0 0 24 24" aria-hidden="true">
        <path d="M12 2a7 7 0 0 0-7 7c0 5 7 13 7 13s7-8 7-13a7 7 0 0 0-7-7zm0 9.5A2.5 2.5 0 1 1 12 6.5a2.5 2.5 0 0 1 0 5z" fill="var(--text-soft)"/>
      </svg>
      <div>Av. das Palmeiras, 95, Conj. 44<br>Jardim, SP CEP 04500-000</div>
    </div>

    <div class="contact contact--phone">
      <svg width="18" height="18" viewBox="0 0 24 24" aria-hidden="true">
        <path d="M6.6 10.8a15 15 0 0 0 6.6 6.6l2.2-2.2a1 1 0 0 1 1-.25 11.4 11.4 0 0 0 3.6.57 1 1 0 0 1 1 1V20a1 1 0 0 1-1 1A17 17 0 0 1 3 4a1 1 0 0 1 1-1h3.5a1 1 0 0 1 1 1c0 1.25.2 2.45.57 3.57a1 1 0 0 1-.25 1z" fill="var(--text-soft)"/>
      </svg>
      <div>(11) 4321-7788<br>(11) 97654-1122</div>
    </div>

    <div class="rule"></div>
    <div class="email">contato@vilaprumo.com.br</div>
  </div>
</body>
</html>
```